Energieberater sucht Flyer-Design
Zielgruppe
Ich bin Energieberater, habe mich vor kurzem selbstständig gemacht und möchte nun meine Bekanntheit steigern. Meine Zielgruppe sind Immobilieneigentümer sowie Immobiliensuchende, welchen ich eine fundierte Energieberatung mit Sanierungskonzepten sowie die Erstellung von Energieausweisen bieten kann.
Aufgabenstellung
Ich benötige einen Flyer, welchen ich regional verteilen möchte. Der Flyer soll quadratisch (148 x 148) erstellt werden.
Der Flyer sollte mein Logo, meine Kontaktdaten, die unten aufgeführten Dienstleistungen sowie einen Gutschein enthalten und insbesondere der Bekanntheits-/Imagesteigerung dienen.
Vorhandene Punkte sollen sein:
- Erstellung von Energieausweisen für Vermietung und Verkauf
- Energieberatung
- Sanierungs- und Modernisierungskonzepte
- Fördermittelberatung
Der Flyer soll die Möglichkeit bieten, am Rand abgeschnitten zu werden. Dort soll ein Gutschein aufgeführt werden mit 25 € Rabatt für einen Energieausweis.
Meine Kontaktdaten können Sie der angehängten Visitenkarte entnehmen.

```html
<!DOCTYPE html>
<html lang="de">
<head>
<meta charset="utf-8">
<title>Flyer Energieberatung – Gutschein</title>
<link rel="stylesheet" href="https://fonts.googleapis.com/css2?family=Arimo:wght@400;700&display=swap">
<style>
  :root {
    --teal: #1a7f96;
    --grey: #7b7b7b;
    --grey-light: #8a8a8a;
    --white: #ffffff;
    --ink: #1b1b1b;
    --backdrop: #ececec;
  }
  * { box-sizing: border-box; margin: 0; padding: 0; }
  html, body { width: 1200px; height: 529px; overflow: hidden; }
  body { background: var(--backdrop); font-family: "Arimo", Arial, sans-serif; position: relative; }

  .flyer { position: absolute; left: 0; top: 0; width: 529px; height: 529px; background: var(--white); overflow: hidden; }

  .coupon { position: absolute; left: 0; top: 0; width: 139px; height: 529px; }
  .cut-line { position: absolute; left: 139px; top: 0; height: 529px; border-left: 2px dashed var(--ink); }

  .house-photo {
    position: absolute; left: 142px; top: 0; width: 387px; height: 309px;
    background:
      radial-gradient(ellipse at 30% 45%, #c8412a 0 18%, transparent 32%),
      radial-gradient(ellipse at 85% 80%, #e9a23a 0 12%, transparent 30%),
      linear-gradient(160deg, #e9eef3 0%, #c9d7e4 55%, #a9bfd3 100%);
  }

  .brand {
    position: absolute; left: 246px; top: 0; width: 189px; height: 48px;
    background: var(--white); display: flex; align-items: center; gap: 8px; padding: 0 10px;
  }
  .brand-mark { width: 22px; height: 22px; background: var(--teal); flex: none; }
  .brand-name { font-size: 11px; font-weight: 700; color: var(--teal); letter-spacing: .04em; line-height: 1.25; text-transform: uppercase; }

  .services { position: absolute; left: 142px; top: 236px; width: 249px; list-style: none; }
  .service {
    height: 48px; margin-bottom: 4px; background: var(--grey);
    color: var(--white); font-size: 13px; line-height: 1.2;
    display: flex; align-items: center; padding: 0 14px;
    opacity: .96;
  }
  .service:nth-child(3), .service:nth-child(4) { height: 50px; }

  .contact-rule { position: absolute; left: 246px; top: 468px; width: 283px; height: 3px; background: var(--teal); }
  .contact-divider { position: absolute; left: 428px; top: 478px; width: 1px; height: 36px; background: var(--ink); }
  .contact { position: absolute; top: 482px; font-size: 9.5px; font-weight: 700; color: var(--ink); line-height: 1.35; text-align: center; }
  .contact-reach { left: 248px; width: 178px; }
  .contact-address { left: 432px; width: 94px; }
  .contact-bottom { position: absolute; left: 246px; top: 518px; width: 283px; height: 2px; background: var(--teal); }
</style>
</head>
<body>
  <section class="flyer">
    <svg class="coupon" viewBox="0 0 139 529" width="139" height="529">
      <rect x="0" y="0" width="139" height="14" fill="var(--teal)"/>
      <rect x="69" y="25" width="51" height="284" fill="var(--grey-light)"/>
      <text transform="translate(56 309) rotate(-90)" font-family="Arimo, Arial, sans-serif" font-size="34" fill="var(--teal)">für Ihren</text>
      <text transform="translate(110 296) rotate(-90)" font-family="Arimo, Arial, sans-serif" font-size="34" fill="var(--white)">Energieausweis</text>
      <rect x="0" y="320" width="139" height="209" fill="var(--teal)"/>
      <text transform="translate(82 505) rotate(-90)" font-family="Arimo, Arial, sans-serif" font-size="76" font-weight="700" fill="var(--white)">25 €</text>
      <text transform="translate(126 513) rotate(-90)" font-family="Arimo, Arial, sans-serif" font-size="46" font-weight="700" fill="var(--white)">Rabatt</text>
    </svg>
    <div class="cut-line"></div>

    <div class="house-photo" role="img" aria-label="Foto: Modellhaus mit rotem Dach auf Bauplänen vor farbiger Energieeffizienzskala"></div>

    <div class="brand">
      <span class="brand-mark"></span>
      <span class="brand-name">Energieberatung<br>Jonas Werling</span>
    </div>

    <ul class="services">
      <li class="service">Sanierungs- und<br>Modernisierungskonzepte</li>
      <li class="service">Erstellung von Energieausweisen<br>für Vermietung und Verkauf</li>
      <li class="service">Fördermittelberatung</li>
      <li class="service">Energieberatung</li>
    </ul>

    <div class="contact-rule"></div>
    <p class="contact contact-reach">+49 0151 47260391<br>info@energieberatung-werling.com<br>www.energieberatung-werling.com</p>
    <div class="contact-divider"></div>
    <p class="contact contact-address">Am Lindenhang<br>35712 Hainbach</p>
    <div class="contact-bottom"></div>
  </section>
</body>
</html>
```